Harlow Grading LLC business card design

Excavation company business cards

Contact Information for Business Card

Harlow Grading LLC cell phone 208-471-9360 office phone 208-396-4815 harlowgradingllc@mailverde.net Driveways, site prep, retaining walls, septic systems, rock delivery

Colors

Designer to choose colors to be used in the design.

```html
<!DOCTYPE html>
<html lang="en">
<head>
<meta charset="utf-8">
<title>Harlow Grading LLC – Business Card</title>
<link href="https://fonts.googleapis.com/css2?family=Montserrat:wght@400;500;700;800&display=swap" rel="stylesheet">
<style>
  :root {
    --backdrop: #d3d3d3;
    --card-black: #0b0b0b;
    --card-white: #f1f1f1;
    --orange: #e8621c;
    --steel: #5f5f5f;
    --ink: #3a3a3a;
    --rule: #bdbdbd;
  }
  * { box-sizing: border-box; margin: 0; padding: 0; }
  html, body { width: 1084px; height: 1200px; overflow: hidden; }
  body {
    background: var(--backdrop);
    font-family: "Montserrat", sans-serif;
    position: relative;
  }
  .card {
    position: absolute;
    left: 112px;
    width: 860px;
    height: 491px;
    border-radius: 28px;
    overflow: hidden;
    box-shadow: 0 6px 14px rgba(0,0,0,0.28);
  }
  /* Back side */
  .card-back { top: 80px; background: var(--card-black); }
  .back-pattern {
    position: absolute; inset: 0;
    background: radial-gradient(ellipse at 85% 35%, #262626 0%, #121212 45%, #0b0b0b 80%);
  }
  .back-brand {
    position: absolute;
    left: 458px; top: 270px;
    display: flex; align-items: center; gap: 10px;
  }
  .brand-mark { width: 22px; height: 22px; background: var(--orange); }
  .brand-name {
    font-weight: 800; color: var(--orange);
    font-size: 27px; letter-spacing: 0.5px; text-transform: uppercase;
  }
  /* Front side */
  .card-front { top: 629px; background: var(--card-white); }
  .front-brand {
    position: absolute; left: 71px; top: 95px;
    display: flex; align-items: center; gap: 12px;
  }
  .front-brand .brand-mark { width: 28px; height: 28px; }
  .front-brand .brand-name { font-size: 34px; }
  .person {
    position: absolute; right: 63px; top: 200px; text-align: right;
  }
  .person-name { font-size: 31px; font-weight: 500; color: var(--orange); line-height: 1.1; }
  .person-title { font-size: 21px; color: var(--ink); margin-top: 3px; }
  .divider {
    position: absolute; left: 54px; right: 63px; top: 288px;
    height: 2px; background: var(--rule);
  }
  .contacts {
    position: absolute; left: 54px; top: 300px; list-style: none;
  }
  .contacts li {
    display: flex; align-items: center; gap: 14px;
    font-size: 19px; color: var(--ink); height: 28px;
  }
  .contacts svg { width: 16px; height: 16px; fill: var(--orange); flex: none; }
  .service-band { position: absolute; left: 0; bottom: 0; width: 860px; height: 36px; }
  .service-text {
    position: absolute; left: 0; right: 0; bottom: 7px;
    text-align: center; color: #fff; font-size: 14.5px; letter-spacing: 0.2px;
    text-transform: uppercase;
  }
</style>
</head>
<body>

<section class="card card-back" aria-label="Card back">
  <div class="back-pattern" role="img" aria-label="Faint tiled pattern of excavator and mountain emblems on black"></div>
  <div class="back-brand">
    <span class="brand-mark"></span>
    <span class="brand-name">Harlow Grading</span>
  </div>
</section>

<section class="card card-front" aria-label="Card front">
  <div class="front-brand">
    <span class="brand-mark"></span>
    <span class="brand-name">Harlow Grading</span>
  </div>

  <div class="person">
    <p class="person-name">Wade Corbin</p>
    <p class="person-title">President</p>
  </div>

  <div class="divider"></div>

  <ul class="contacts">
    <li>
      <svg viewBox="0 0 24 24"><path d="M6.6 10.8a15.1 15.1 0 0 0 6.6 6.6l2.2-2.2a1 1 0 0 1 1-.25 11.4 11.4 0 0 0 3.6.57 1 1 0 0 1 1 1V20a1 1 0 0 1-1 1A17 17 0 0 1 3 4a1 1 0 0 1 1-1h3.5a1 1 0 0 1 1 1c0 1.25.2 2.45.57 3.57a1 1 0 0 1-.25 1z"/></svg>
      208-471-9360
    </li>
    <li>
      <svg viewBox="0 0 24 24"><path d="M6.6 10.8a15.1 15.1 0 0 0 6.6 6.6l2.2-2.2a1 1 0 0 1 1-.25 11.4 11.4 0 0 0 3.6.57 1 1 0 0 1 1 1V20a1 1 0 0 1-1 1A17 17 0 0 1 3 4a1 1 0 0 1 1-1h3.5a1 1 0 0 1 1 1c0 1.25.2 2.45.57 3.57a1 1 0 0 1-.25 1z"/></svg>
      208-396-4815
    </li>
    <li>
      <svg viewBox="0 0 24 24"><path d="M2 5h20v14H2z M3.5 6.5 12 13l8.5-6.5" stroke="#f1f1f1" stroke-width="1.4"/></svg>
      harlowgradingllc@mailverde.net
    </li>
    <li>
      <svg viewBox="0 0 24 24"><circle cx="12" cy="12" r="10"/><path d="M2 12h20M12 2c3 3 3 17 0 20M12 2c-3 3-3 17 0 20M4 7h16M4 17h16" stroke="#f1f1f1" stroke-width="1.2" fill="none"/></svg>
      HarlowGradingLLC.net
    </li>
  </ul>

  <svg class="service-band" viewBox="0 0 860 36" aria-hidden="true">
    <g fill="var(--steel)">
      <polygon points="0,36 18,0 30,0 12,36"/>
      <polygon points="24,36 42,0 54,0 36,36"/>
      <polygon points="48,36 66,0 78,0 60,36"/>
      <polygon points="72,36 90,0 102,0 84,36"/>
      <polygon points="772,36 790,0 802,0 784,36"/>
      <polygon points="796,36 814,0 826,0 808,36"/>
      <polygon points="820,36 838,0 850,0 832,36"/>
      <polygon points="844,36 860,4 860,28 856,36"/>
    </g>
    <polygon fill="var(--orange)" points="96,36 114,0 772,0 754,36"/>
  </svg>
  <p class="service-text">Driveways • Site Prep • Retaining Walls • Septic Systems • Rock Delivery</p>
</section>

</body>
</html>
```